Business Card design for law firm = Juriskite Australia

We are seeking a new design for our business cards.
We are keeping our logo, which is attached.
We need space for
Name
Title
Address is , which is
Level 14
82 Penhallow Street
Sydney NSW 2000
Phone :
Mobile :
Fax :
Email :
DX :
website www.juriskite.com.au

Industry/Entity Type

Law Firm / Banking and Finance

Contact Information for Business Card

We are seeking a new design for our business cards. We are keeping our logo. We need space for Name Title Address is Level 14 82 Penhallow Street Sydney NSW 2000 Phone Mobile Fax Email DX website www.juriskite.com.au

Colors
0054AA
0677BA
7BADD7
CADEEF
E8F1F8

Requirements
Must have
• see our website for general feel www.juriskite.com.au

```html
<!DOCTYPE html>
<html lang="en">
<head>
<meta charset="utf-8">
<title>Juriskite Australia – Business Card</title>
<link href="https://fonts.googleapis.com/css2?family=Crimson+Pro:wght@400&family=Mulish:wght@400;500&display=swap" rel="stylesheet">
<style>
  :root {
    --brand-blue: #1f5aa6;
    --brand-deep: #0054aa;
    --brand-teal: #0677ba;
    --brand-navy: #0d3f86;
    --brand-pale: #cadeef;
    --paper: #ffffff;
    --paper-shade: #eef1f4;
    --ink: #2b2f36;
    --backdrop: #d9dde2;
    --serif: "Crimson Pro", Georgia, serif;
    --sans: "Mulish", Arial, sans-serif;
  }
  * { margin: 0; padding: 0; box-sizing: border-box; }
  html, body { width: 1200px; height: 900px; overflow: hidden; background: var(--backdrop); }
  .stage { position: relative; width: 1200px; height: 900px; }
  .card {
    position: absolute; left: 250px; width: 700px; height: 400px;
    overflow: hidden; box-shadow: 0 6px 18px rgba(0,0,0,.18);
  }
  .card--front { top: 35px; background: var(--brand-blue); color: var(--paper); }
  .card--back { top: 465px; background: linear-gradient(120deg, var(--paper-shade), var(--paper) 60%); }

  /* front */
  .front__wordmark {
    position: absolute; left: 0; right: 0; top: 112px; text-align: center;
    font-family: var(--serif); font-size: 88px; letter-spacing: 1px; line-height: 1;
  }
  .front__tagline {
    position: absolute; left: 0; right: 0; top: 208px; text-align: center;
    font-family: var(--sans); font-size: 25px; letter-spacing: 3px; white-space: nowrap;
  }
  .front__rule {
    position: absolute; left: 140px; right: 90px; top: 258px; height: 2px; background: var(--brand-teal);
  }
  .front__web {
    position: absolute; left: 0; right: 0; top: 276px; text-align: center;
    font-family: var(--sans); font-weight: 500; font-size: 15px; letter-spacing: 3.5px;
  }

  /* back */
  .back__panel { position: absolute; inset: 0; }
  .back__wordmark {
    position: absolute; left: 466px; top: 64px; white-space: nowrap;
    font-family: var(--serif); font-size: 54px; color: var(--brand-deep); line-height: 1;
  }
  .back__tagline {
    position: absolute; left: 468px; top: 126px; white-space: nowrap; font-family: var(--sans);
    font-size: 14px; letter-spacing: 1px; color: var(--brand-teal);
  }
  .back__address {
    position: absolute; right: 36px; top: 222px; text-align: right; font-style: normal;
    font-family: var(--sans); font-size: 16px; line-height: 1.5; color: var(--ink);
  }
  .person { position: absolute; left: 58px; top: 170px; color: var(--paper); }
  .person__rule { width: 190px; height: 2px; background: var(--paper); margin-bottom: 8px; }
  .person__name { font-family: var(--serif); font-size: 30px; line-height: 1.05; }
  .person__title { font-family: var(--sans); font-size: 15px; letter-spacing: .5px; margin-top: 4px; }
  .contacts {
    position: absolute; left: 150px; list-style: none; color: var(--paper);
    font-family: var(--sans); font-size: 16px; line-height: 1.55; white-space: nowrap;
  }
  .contacts--phone { top: 240px; }
  .contacts--web { top: 325px; }
  .contacts li { display: flex; align-items: center; gap: 9px; }
  .contacts svg { width: 13px; height: 13px; fill: var(--brand-pale); flex: none; }
</style>
</head>
<body>
<main class="stage">

  <section class="card card--front" aria-label="Card front">
    <div class="front__wordmark">Juriskite</div>
    <div class="front__tagline">strategic legal outsourcing</div>
    <div class="front__rule"></div>
    <div class="front__web">www.juriskite.com.au</div>
  </section>

  <section class="card card--back" aria-label="Card back">
    <svg class="back__panel" viewBox="0 0 700 400" width="700" height="400" aria-hidden="true">
      <polygon points="0,0 318,0 452,76 418,400 406,400 441,80 308,0" fill="var(--brand-teal)"/>
      <polyline points="300,0 436,84 402,400" fill="none" stroke="var(--brand-navy)" stroke-width="2"/>
      <polygon points="0,0 300,0 436,84 402,400 0,400" fill="var(--brand-blue)"/>
    </svg>

    <div class="back__wordmark">Juriskite</div>
    <div class="back__tagline">strategic legal outsourcing</div>

    <address class="back__address">
      Level 14<br>82 Penhallow Street<br>Sydney NSW 2000<br>DX 318 Sydney
    </address>

    <div class="person">
      <div class="person__rule"></div>
      <div class="person__name">Liam Carrow</div>
      <div class="person__title">Managing Director</div>
    </div>

    <ul class="contacts contacts--phone">
      <li><svg viewBox="0 0 16 16"><path d="M3 1h3l1.5 4-2 1.2a9 9 0 0 0 4.3 4.3L11 8.5l4 1.5v3a2 2 0 0 1-2 2A12 12 0 0 1 1 3a2 2 0 0 1 2-2z"/></svg>02 9417 3380</li>
      <li><svg viewBox="0 0 16 16"><path d="M4 0h8a1 1 0 0 1 1 1v14a1 1 0 0 1-1 1H4a1 1 0 0 1-1-1V1a1 1 0 0 1 1-1zm1 2v10h6V2z"/></svg>02 9417 5521</li>
      <li><svg viewBox="0 0 16 16"><path d="M4 1h7l2 2v3h1a2 2 0 0 1 2 2v6H0V8a2 2 0 0 1 2-2h2zm1 1v4h7V3.5L10.5 2zm-2 7v2h3V9z"/></svg>02 9418 2750</li>
    </ul>
    <ul class="contacts contacts--web">
      <li><svg viewBox="0 0 16 16"><path d="M1 3h14v10H1zm1.5 1.2V5l5.5 4 5.5-4v-.8z"/></svg>enquiries@juriskite.com.au</li>
      <li><svg viewBox="0 0 16 16"><path d="M8 0a8 8 0 1 1 0 16A8 8 0 0 1 8 0zM2 7h3a12 12 0 0 1 1.5-5A6 6 0 0 0 2 7zm4.5 0h3A10 10 0 0 0 8 2a10 10 0 0 0-1.5 5zm0 2A10 10 0 0 0 8 14a10 10 0 0 0 1.5-5zM11 7h3a6 6 0 0 0-4.5-5A12 12 0 0 1 11 7zm0 2a12 12 0 0 1-1.5 5A6 6 0 0 0 14 9zM2 9a6 6 0 0 0 4.5 5A12 12 0 0 1 5 9z"/></svg>www.juriskite.com.au</li>
    </ul>
  </section>

</main>
</body>
</html>
```